PowerPoint presentation in support of a $6 million capital raise for the acquisition of a business

I need a combination logo design and PowerPoint presentation design. The company name is Brevant Capital Partners, LLC. I have populated the PowerPoint with most of the information, but it's ugly and crowded. I want it to sizzle and look very professional.

I will need to provide additional content, including financial information, during the task. It is not quite finished.

Target Market(s)

sophisticated investors

Industry/Entity Type

Financial

```html
<!DOCTYPE html>
<html lang="en">
<head>
<meta charset="utf-8">
<title>The Title Loan Business Model</title>
<link href="https://fonts.googleapis.com/css2?family=Libre+Baskerville:wght@400;700&display=swap" rel="stylesheet">
<style>
  :root {
    --slide-bg: #ffffff;
    --frame-dark: #000000;
    --accent-orange: #ff9500;
    --accent-dot: #fb8c4e;
    --title-blue: #4f7dc1;
    --title-blue-deep: #2d5a9e;
    --logo-ink: #1b3f7a;
    --body-ink: #111111;
    --stripe-peach: #f9cdb8;
    --stripe-light: #fde7dc;
    --stripe-line: #ef9f7c;
    --bullet-a: #e8c88a;
    --bullet-b: #b08a48;
  }
  html, body {
    margin: 0;
    padding: 0;
    width: 1200px;
    height: 900px;
    overflow: hidden;
    background: var(--slide-bg);
  }
  .slide {
    position: relative;
    width: 1200px;
    height: 900px;
    overflow: hidden;
    background: var(--slide-bg);
    font-family: "Libre Baskerville", Georgia, serif;
    color: var(--body-ink);
  }
  .edge-left {
    position: absolute;
    left: 0; top: 33px;
    width: 4px; height: 828px;
    background: var(--frame-dark);
  }
  .edge-bottom {
    position: absolute;
    left: 0; bottom: 0;
    width: 1200px; height: 39px;
    background: var(--frame-dark);
  }
  .side-stripes {
    position: absolute;
    top: 0; right: 0;
    width: 54px; height: 861px;
  }
  .logo {
    position: absolute;
    left: 35px; top: 10px;
    width: 235px; height: 122px;
    border-radius: 26px;
    background: var(--accent-orange);
    display: flex;
    align-items: center;
    justify-content: center;
  }
  .logo-name {
    font-size: 54px;
    font-weight: 400;
    color: var(--logo-ink);
    letter-spacing: 2px;
  }
  .slide-title {
    position: absolute;
    left: 330px; top: 76px;
    margin: 0;
    font-size: 43px;
    font-weight: 700;
    letter-spacing: 1px;
    color: var(--title-blue);
    text-shadow: 1px 1px 0 #ffffff, 2px 2px 2px rgba(45, 90, 158, 0.45);
    white-space: nowrap;
  }
  .lead {
    position: absolute;
    left: 33px; top: 205px;
    margin: 0;
    font-size: 24px;
    font-weight: 700;
    text-decoration: underline;
    text-underline-offset: 4px;
    white-space: nowrap;
  }
  .points {
    position: absolute;
    left: 42px; top: 276px;
    width: 1100px;
    margin: 0; padding: 0;
    list-style: none;
    font-size: 23px;
    line-height: 35.5px;
  }
  .points li {
    margin-bottom: 13px;
  }
  .points li::before {
    content: "";
    display: inline-block;
    width: 15px; height: 13px;
    margin-right: 3px;
    vertical-align: 1px;
    background: linear-gradient(135deg, var(--bullet-a), var(--bullet-b));
  }
  .points li.narrow { width: 1000px; }
  .accent-dot {
    position: absolute;
    left: 1070px; top: 750px;
    width: 71px; height: 71px;
    border-radius: 50%;
    background: var(--accent-dot);
  }
</style>
</head>
<body>
<main class="slide">
  <div class="edge-left"></div>
  <svg class="side-stripes" viewBox="0 0 54 861" aria-hidden="true">
    <rect x="0" y="0" width="54" height="861" fill="var(--stripe-light)"/>
    <rect x="0" y="0" width="3" height="861" fill="var(--stripe-line)"/>
    <rect x="7" y="0" width="8" height="861" fill="var(--stripe-peach)"/>
    <rect x="20" y="0" width="4" height="861" fill="#ffffff"/>
    <rect x="27" y="0" width="3" height="861" fill="var(--stripe-line)"/>
    <rect x="34" y="0" width="20" height="861" fill="var(--stripe-peach)"/>
  </svg>

  <div class="logo"><span class="logo-name">BCP</span></div>
  <h1 class="slide-title">The Title Loan Business Model</h1>

  <p class="lead">The title loan business model operates (generally) as follows:</p>

  <ul class="points">
    <li>Loans averaging $950 equal to 20% to 60% of the auction (liquidation) value of the borrowers auto are made at rates averaging 20% per month for an average duration of approximately 6 months</li>
    <li>The lender takes the borrower through a process to verify ownership and a clean title, photograph the automobile, determine value, secure the physical title, obtain a spare ignition key and gather appropriate information regarding the borrower</li>
    <li>The borrower makes monthly payments pursuant to the terms of the loan; if the borrower fails to pay the loan as required, the lender will move to repossess the collateral and liquidate it to satisfy the loan amount plus interest and repossession fees</li>
    <li>Bad loans average 6% of total loans and 20% of gross revenues</li>
    <li class="narrow">Gross profit of 80% and net income (before taxes) of 40% is typical for a mature, well run title loan business</li>
  </ul>

  <div class="accent-dot"></div>
  <div class="edge-bottom"></div>
</main>
</body>
</html>
```